Single brochure for international companies in the financial sector

We need to update a brochure 4 pages presenting our company. We are a financial engineering company. The final design must provide financial security, service and trust. you will find the current brochure copy. Our color code is Orange (RGB 235/100/68), Black, White and Gray. photos show the visual of the site, but it is not mandatory to keep them.

Target Market(s)

wealth management professionals

Industry/Entity Type

Finance

Requirements
Must have
• Logo Velbrook Capital all text in the document color Orange Velbrook (RGB 235/100/68)
Nice to have
• Vista Font
Should not have
• images / pictures of people

```html
<!DOCTYPE html>
<html lang="en">
<head>
<meta charset="utf-8">
<title>Velbrook Capital — Brochure</title>
<link rel="stylesheet" href="https://fonts.googleapis.com/css2?family=Josefin+Sans:wght@300;400&family=Libre+Baskerville:wght@400;700&family=Merriweather:wght@300;400;700&display=swap">
<style>
  :root{
    --orange:#eb6444;
    --black:#1b1b1b;
    --ink:#3a3a3a;
    --white:#ffffff;
    --paper:#f4f4f4;
    --gray:#c9c9c9;
    --stage:#d6d6d6;
    --photo-light:#d9d9d9;
    --photo-mid:#a9a9a9;
    --photo-dark:#4a4a4a;
  }
  *{box-sizing:border-box;margin:0;padding:0}
  html,body{width:1200px;height:2394px;overflow:hidden;background:var(--stage)}
  body{position:relative;font-family:"Merriweather",Georgia,serif;color:var(--ink)}

  .page{position:absolute;overflow:hidden;background:var(--paper);box-shadow:0 10px 30px rgba(0,0,0,.18)}
  .spread{position:absolute;left:60px;width:1080px;height:540px;display:flex;box-shadow:0 10px 30px rgba(0,0,0,.18)}
  .spread .page{position:relative;width:540px;height:540px;box-shadow:none}

  /* Front cover */
  .cover{font-size:20px}
  .cover__head{position:absolute;left:0;top:0;width:100%;height:48%;background:var(--white);text-align:center;padding-top:3.2em}
  .brand{display:inline-flex;align-items:center;gap:.7em;font-family:"Josefin Sans",Arial,sans-serif;font-weight:300;color:var(--orange);letter-spacing:.38em;font-size:1.75em;line-height:1}
  .brand__mark{width:.45em;height:.45em;background:var(--orange)}
  .cover__rule{width:3.4em;height:2px;background:var(--black);margin:1.3em auto 1.1em}
  .cover__tag{font-family:"Libre Baskerville",Georgia,serif;font-size:.55em;letter-spacing:.3em;color:var(--ink)}
  .cover__photo{position:absolute;left:0;bottom:0;width:100%;height:52%;
    background:linear-gradient(180deg,var(--photo-light) 0%,var(--photo-mid) 48%,var(--photo-dark) 58%,var(--photo-mid) 70%,var(--photo-light) 100%)}

  /* Back cover */
  .back{background:var(--orange);font-size:15px}
  .back__art{position:absolute;left:6%;bottom:0;width:40%;height:78%;
    background:linear-gradient(180deg,rgba(90,20,10,.25),rgba(90,20,10,.55))}
  .back__legal{position:absolute;left:34%;bottom:7%;font-family:"Libre Baskerville",Georgia,serif;font-size:.62em;letter-spacing:.28em;line-height:1.8;color:var(--white)}

  /* Inside left */
  .inside-left{background:var(--white);font-size:15px;padding:3.4em 3em 0 4em}
  .company__title{font-family:"Libre Baskerville",Georgia,serif;font-weight:400;font-size:1.9em;letter-spacing:.04em;color:var(--black)}
  .company__rule{width:5.5em;height:1px;background:var(--ink);margin:.9em 0 0 1.4em}
  .company__body{text-align:center;margin:1.2em 0 0 3em;width:20em}
  .quote-mark{font-family:"Libre Baskerville",Georgia,serif;font-size:2.2em;color:var(--gray);line-height:.8}
  .lead{font-weight:700;font-size:.72em;line-height:1.55;color:var(--black);margin-bottom:1.6em}
  .label{font-family:"Josefin Sans",Arial,sans-serif;font-size:.66em;letter-spacing:.3em;color:var(--black);margin-bottom:.7em}
  .copy{font-weight:300;font-size:.66em;line-height:1.7;color:var(--ink);margin-bottom:1.7em}
  .punch{font-family:"Merriweather",Georgia,serif;font-size:.9em;color:var(--orange)}

  /* Inside right */
  .inside-right{background:var(--white);font-size:15px;padding:3.2em 2.6em}
  .services{text-align:center}
  .services .label{margin-bottom:.8em}
  .grid{display:grid;grid-template-columns:1fr 1fr;margin:1.8em 0 1.8em;border-top:1px solid var(--ink)}
  .grid__cell{padding:1.4em 1.1em 0}
  .grid__cell + .grid__cell{border-left:1px solid var(--ink)}

  .front-single{left:240px;top:120px;width:720px;height:720px}
  .spread--inside{top:990px}
  .spread--outside{top:1680px}
</style>
</head>
<body>

  <!-- Front cover -->
  <section class="page cover front-single">
    <div class="cover__head">
      <div class="brand"><span class="brand__mark"></span>VELBROOK CAPITAL</div>
      <div class="cover__rule"></div>
      <div class="cover__tag">FINANCIAL ENGINEERING</div>
    </div>
    <div class="cover__photo" role="img" aria-label="Black and white long-exposure photograph of a long arched bridge over still water"></div>
  </section>

  <!-- Inside spread -->
  <div class="spread spread--inside">
    <section class="page inside-left">
      <h1 class="company__title">THE COMPANY.</h1>
      <div class="company__rule"></div>
      <div class="company__body">
        <div class="quote-mark">&ldquo;</div>
        <p class="lead">Our clients must deliver performance on their portfolios on a regular basis.<br>We help them deliver everyday.</p>
        <h2 class="label">ABOUT US</h2>
        <p class="copy">Velbrook Capital is a financial engineering company.<br>It is fully independent from any bank or any other company.</p>
        <h2 class="label">WHAT WE DO</h2>
        <p class="copy">We provide them with investment solutions designed to improve their portfolios performance.</p>
        <p class="punch">Simple as that.</p>
      </div>
    </section>

    <section class="page inside-right services">
      <h2 class="label">OUR CLIENTS</h2>
      <p class="copy">Our clients are international companies, institutionals, corporates, private banks and wealth managers. Our purpose is to make their work easier every day.</p>
      <div class="grid">
        <div class="grid__cell">
          <h2 class="label">INVESTMENT ADVICE</h2>
          <p class="copy">Each client is looking for a unique solution. We listen to their constraints and targets, then we design tailored products that offer a truly independent answer, simple and efficient.</p>
        </div>
        <div class="grid__cell">
          <h2 class="label">PORTFOLIO ANALSIS</h2>
          <p class="copy">We advise our clients on their portfolios of financial products. Together we identify the needs for restructuring or reallocating the assets. We also provide full monitoring and reporting services throughout the life of the products.</p>
        </div>
      </div>
      <h2 class="label">PARTNER SELECTION</h2>
      <p class="copy">Our internal tools allow us to continuously assess the issuers we are working with. Therefore we give our clients the best issuers for their investment solutions.</p>
    </section>
  </div>

  <!-- Outside spread -->
  <div class="spread spread--outside">
    <section class="page back">
      <div class="back__art" role="img" aria-label="Dark silhouette illustration of the Eiffel Tower on the orange page"></div>
      <p class="back__legal">
        VELBROOK CAPITAL SA.<br>
        CAPITAL : 400 000 EUROS<br>
        RCS PARIS : 812 447 205<br>
        CODE BANQUE (CIB) : 14072<br>
        WWW.VELBROOKCAPITAL.COM
      </p>
    </section>
    <section class="page cover" style="font-size:15px">
      <div class="cover__head">
        <div class="brand"><span class="brand__mark"></span>VELBROOK CAPITAL</div>
        <div class="cover__rule"></div>
        <div class="cover__tag">FINANCIAL ENGINEERING</div>
      </div>
      <div class="cover__photo" role="img" aria-label="Black and white long-exposure photograph of a long arched bridge over still water"></div>
    </section>
  </div>

</body>
</html>
```